Navelo Partnering Business Card

Hello everyone. We need a business card design that would match our logo and the theme we're trying to have for Navelo that you can find on our website and/or Corvapage page

```html
<!DOCTYPE html>
<html lang="en">
<head>
<meta charset="UTF-8">
<title>Navelo Business Card</title>
<link rel="stylesheet" href="https://fonts.googleapis.com/css2?family=Montserrat:wght@400;600;700&display=swap">
<style>
  :root {
    --canvas-bg: #efeff1;
    --card-navy: #08072c;
    --brand-gold: #e0a21a;
    --text-white: #f2f2f5;
  }
  * { margin: 0; padding: 0; box-sizing: border-box; }
  html, body {
    width: 1200px;
    height: 1200px;
    overflow: hidden;
    background: var(--canvas-bg);
    font-family: "Montserrat", Arial, sans-serif;
  }
  .canvas {
    position: relative;
    width: 1200px;
    height: 1200px;
  }
  .card {
    position: absolute;
    top: 311px;
    width: 371px;
    height: 577px;
    background: var(--card-navy);
  }
  .card--front { left: 150px; }
  .card--back { left: 657px; }

  .brand-name {
    position: absolute;
    left: 0;
    width: 316px;
    text-align: center;
    font-family: "Montserrat", Arial, sans-serif;
    font-weight: 600;
    font-size: 52px;
    letter-spacing: -0.5px;
    line-height: 1;
  }
  .card--front .brand-name {
    top: 83px;
    color: var(--brand-gold);
  }
  .card--back .brand-name {
    top: 251px;
    color: var(--text-white);
  }

  .contact-list {
    position: absolute;
    left: 0;
    top: 375px;
    width: 356px;
    text-align: center;
    list-style: none;
  }
  .contact-item { margin-bottom: 20px; }
  .contact-item:nth-child(2) { margin-bottom: 12px; }
  .contact-label {
    display: block;
    color: var(--brand-gold);
    font-weight: 700;
    font-size: 20px;
    line-height: 24px;
  }
  .contact-value {
    display: block;
    color: var(--text-white);
    font-weight: 400;
    font-size: 16px;
    letter-spacing: 0.6px;
    line-height: 20px;
  }
</style>
</head>
<body>
  <main class="canvas">
    <section class="card card--front" aria-label="Card front">
      <div class="brand-name">Navelo</div>
      <ul class="contact-list">
        <li class="contact-item">
          <span class="contact-label">Phone:</span>
          <span class="contact-value">(01) 4050 4050</span>
        </li>
        <li class="contact-item">
          <span class="contact-label">Web:</span>
          <span class="contact-value">www.navelo.com</span>
        </li>
        <li class="contact-item">
          <span class="contact-label">Email:</span>
          <span class="contact-value">sample@navelo.com</span>
        </li>
      </ul>
    </section>
    <section class="card card--back" aria-label="Card back">
      <div class="brand-name">Navelo</div>
    </section>
  </main>
</body>
</html>
```